Modern, Clean, Edgy & Fun Comedy Show Flyer

We need to a create a new flyer for the comedy show, Harbor Laugh Nights. The original version of the flyer is attached (file: Old flyer), as well as two versions of the logo.
- The text should be the same except now the show is Every First Wednesday and the next show is June 1.
- Remove the jerk shop logo
- Remove the picture of the man, and replace it with a photo of Dale (our host), the Audience, or something of your own design.
* pictures of Dale and the Audience is attached.
* We'd like to keep the same color palette and have also attached a color palette for reference

I have also attached 4 references of flyers that I like, that you can use to get an idea of the theme and aesthetic we are looking for.
* Files: Reference 1, Reference 2, Reference 3, Reference 4
Updates

Colors
3277b5
85acd3
0455a3
eaf1f7
cee9f5
ecf7fb
d5d5d5
e6e6e6

Requirements
Must have
• The harbor laugh nights logo attached
• The text as specified in the project description
• An option with Dale and without

```html
<!DOCTYPE html>
<html lang="en">
<head>
<meta charset="utf-8">
<title>Harbor Laugh Nights – Comedy Show Flyer</title>
<link href="https://fonts.googleapis.com/css2?family=Oswald:wght@400;500&family=Righteous&display=swap" rel="stylesheet">
<style>
  :root {
    --ink: #0b0b0b;
    --paper: #ffffff;
    --brand-blue: #1449d6;
    --photo-ceiling: #2a2a2a;
    --photo-wall: #6e6e6e;
    --photo-glow: rgba(190,190,190,0.45);
    --photo-crowd: #3a3a3a;
    --photo-floor: #161616;
    --venue-grey: #5c5c5c;
  }
  html, body {
    margin: 0;
    padding: 0;
    width: 1200px;
    height: 837px;
    overflow: hidden;
    background: var(--ink);
  }
  .flyer {
    position: relative;
    width: 1200px;
    height: 837px;
    overflow: hidden;
    font-family: "Oswald", "Arial Narrow", sans-serif;
  }
  .headline-band {
    position: absolute;
    left: 0; top: 0;
    width: 1200px; height: 80px;
    background: var(--paper);
    display: flex;
    align-items: center;
    justify-content: center;
  }
  .headline {
    margin: 0;
    font-family: "Righteous", "Arial Black", sans-serif;
    font-weight: 400;
    font-size: 60px;
    letter-spacing: 1.5px;
    word-spacing: 6px;
    color: var(--ink);
    text-transform: uppercase;
    white-space: nowrap;
    line-height: 1;
  }
  .headline sup {
    font-size: 30px;
    text-transform: lowercase;
    vertical-align: 22px;
  }
  .audience-photo {
    position: absolute;
    left: 0; top: 80px;
    width: 1200px; height: 757px;
    background:
      radial-gradient(ellipse 30% 22% at 20% 45%, var(--photo-glow), transparent 70%),
      radial-gradient(ellipse 45% 25% at 50% 28%, rgba(150,150,150,0.35), transparent 70%),
      radial-gradient(ellipse 60% 30% at 40% 85%, rgba(110,110,110,0.35), transparent 70%),
      linear-gradient(180deg, var(--photo-ceiling) 0%, #444 18%, var(--photo-wall) 42%, var(--photo-crowd) 68%, var(--photo-floor) 100%);
  }
  .night-panel {
    position: absolute;
    left: 0; top: 0;
  }
  .featuring-bar {
    position: absolute;
    left: 0; top: 161px;
    width: 564px; height: 44px;
    background: var(--brand-blue);
  }
  .featuring-bar span {
    position: absolute;
    left: 157px; top: 3px;
    font-family: "Righteous", "Arial Black", sans-serif;
    font-size: 31px;
    line-height: 1.2;
    color: var(--paper);
    text-transform: uppercase;
  }
  .lineup {
    position: absolute;
    left: 157px; top: 222px;
    margin: 0; padding: 0;
    list-style: none;
  }
  .lineup li {
    font-size: 33px;
    font-weight: 400;
    color: var(--paper);
    line-height: 65.5px;
    letter-spacing: -0.5px;
  }
  .show-name {
    position: absolute;
    left: 692px; top: 200px;
    width: 440px;
    margin: 0;
    text-align: center;
    font-size: 72px;
    font-weight: 500;
    color: var(--brand-blue);
    text-transform: uppercase;
    line-height: 1.02;
    letter-spacing: 1px;
  }
  .host {
    position: absolute;
    right: 46px; top: 490px;
    margin: 0;
    font-size: 50px;
    font-weight: 500;
    color: var(--paper);
    letter-spacing: -0.5px;
    line-height: 1;
    white-space: nowrap;
  }
  .show-date {
    position: absolute;
    left: 752px; top: 550px;
    margin: 0;
    font-size: 40px;
    font-weight: 500;
    color: var(--brand-blue);
    text-transform: uppercase;
    letter-spacing: -0.5px;
    line-height: 1;
    white-space: nowrap;
  }
  .venue {
    position: absolute;
    color: var(--venue-grey);
    font-size: 38px;
    font-weight: 500;
    letter-spacing: -0.5px;
    line-height: 1;
    margin: 0;
    white-space: nowrap;
  }
  .venue-name { left: 817px; top: 622px; }
  .venue-address { left: 725px; top: 680px; }
  .venue-entry { left: 711px; top: 730px; display: flex; align-items: center; gap: 22px; }
  .venue-entry .divider {
    width: 5px; height: 34px;
    background: var(--brand-blue);
    transform: translateY(-8px);
  }
</style>
</head>
<body>
<main class="flyer">
  <header class="headline-band">
    <h1 class="headline">Comedy Show Every 1<sup>st</sup> Wednesday</h1>
  </header>

  <div class="audience-photo" role="img" aria-label="Black and white photo of a comedy club audience seated in a brick-walled room with a bar and string lights"></div>

  <svg class="night-panel" width="1200" height="837" viewBox="0 0 1200 837" aria-hidden="true">
    <path fill="#000" d="M717,540 L1200,540 L1200,837 L650,837 L644,800 L652,772 L640,742 L656,712 L648,684 L670,660 L700,632 L728,622 L760,622 L772,608 L776,594 L717,594 Z"/>
  </svg>

  <div class="featuring-bar"><span>Featuring....</span></div>

  <ul class="lineup">
    <li>Marcus Bellamy,</li>
    <li>Adrian Ellis,</li>
    <li>Nolan Greenberg,</li>
    <li>Naveen Prasad,</li>
    <li>Femi Yardley</li>
  </ul>

  <p class="show-name">Harbor Laugh<br>Nights</p>

  <p class="host">Hosted by Dale Whitfield</p>
  <p class="show-date">Wednesday, June 1st</p>

  <p class="venue venue-name">The Tin Lantern</p>
  <p class="venue venue-address">42 Pier Lane, Harborview</p>
  <p class="venue venue-entry"><span>Adm: FREE</span><span class="divider"></span><span>Doors 6:30 PM</span></p>
</main>
</body>
</html>
```